Family Values Poster

Need a poster for my kids (ages 5-8) that says:
Be Smart
Be Kind
Be Curious
Be Grateful
We Love You

fun, but hopefully something that they will keep for a long time

Target Market(s)

my kids

Requirements
Must have
• vertical
Nice to have
• fun and attention grabbing
Should not have
• look cheesy - not a generic inspirational poster

```html
<!DOCTYPE html>
<html lang="en">
<head>
<meta charset="utf-8">
<title>Family Values Poster</title>
<link rel="stylesheet" href="https://fonts.googleapis.com/css2?family=Cinzel:wght@500;600&display=swap">
<style>
  :root {
    --backdrop: #33313a;
    --sun-yellow: #f7e21a;
    --amber: #f8a21c;
    --flame-orange: #f05a16;
    --scarlet: #e3141c;
    --magenta: #d31a5a;
    --violet: #7a1fd6;
    --indigo: #4a1ec2;
    --lettering: #ffffff;
  }
  html, body {
    margin: 0;
    padding: 0;
    width: 1200px;
    height: 1200px;
    overflow: hidden;
    background: var(--backdrop);
  }
  .poster {
    position: absolute;
    left: 196px;
    top: 76px;
    width: 810px;
    height: 1048px;
    overflow: hidden;
  }
  .poster__artwork {
    position: absolute;
    inset: 0;
    background:
      radial-gradient(ellipse 55% 45% at 50% 52%, var(--scarlet) 0%, rgba(227,20,28,0.85) 45%, rgba(227,20,28,0) 100%),
      radial-gradient(ellipse 60% 40% at 90% 10%, var(--sun-yellow) 0%, rgba(247,226,26,0) 100%),
      linear-gradient(180deg,
        var(--amber) 0%,
        var(--flame-orange) 25%,
        var(--scarlet) 50%,
        var(--magenta) 66%,
        var(--violet) 84%,
        var(--indigo) 100%);
  }
  .poster__message {
    position: absolute;
    inset: 0;
    width: 810px;
    height: 1048px;
  }
  .poster__message text {
    font-family: "Cinzel", "Trajan Pro", serif;
    fill: var(--lettering);
    text-anchor: middle;
  }
  .line--verb { font-size: 48px; font-weight: 600; }
  .line--value { font-size: 92px; font-weight: 600; letter-spacing: 0.5px; }
  .line--closing { font-size: 70px; font-weight: 600; }
</style>
</head>
<body>
  <main class="poster">
    <div class="poster__artwork" role="img" aria-label="Abstract painted burst of colour radiating from the centre: yellow and orange at top, red in the middle, magenta and purple at the bottom"></div>
    <svg class="poster__message" viewBox="0 0 810 1048" aria-label="Be Smart, Be Kind, Be Curious, Be Grateful, We Love You">
      <text class="line--verb" x="405" y="191">Be</text>
      <text class="line--value" x="405" y="275">Smart</text>
      <text class="line--verb" x="405" y="362">Be</text>
      <text class="line--value" x="405" y="446">Kind</text>
      <text class="line--verb" x="405" y="530">Be</text>
      <text class="line--value" x="405" y="617">Curious</text>
      <text class="line--verb" x="405" y="700">Be</text>
      <text class="line--value" x="405" y="787">Grateful</text>
      <text class="line--closing" x="405" y="918">We Love You</text>
    </svg>
  </main>
</body>
</html>
```